Business Card Design Project - Brantwell Media

We need a new business card that fits with our new logo. We are a social media agency and consultancy operating in China. We want a fresh and strong business card. Our cards need to be two-sided as we have both English and Chinese language names and addresses on the card, but as with our current business card this does not need to be a mirror-image. Our thoughts go out to a white card on the front where the logo/name is and then using the logo colours for different coloured back-grounds. i.e that the back of the biz card works with the four different colours in the logo.

Attached is the new logo, and also a copy of our old business cards.

Target Market(s)

CEO's, CMO's. media and advertising professionals

Industry/Entity Type

Business

Requirements
Must have
• inclusion of both Chinese and English language
Nice to have
• four different colored versions of the back of the biz card. Our logo has four colors and each of these colors we would like to have a version of.

```html
<!DOCTYPE html>
<html lang="en">
<head>
<meta charset="utf-8">
<title>Brantwell Media — Business Card</title>
<link rel="stylesheet" href="https://fonts.googleapis.com/css2?family=Ubuntu:wght@300;400;500&family=Noto+Sans+SC:wght@400&display=swap">
<style>
  :root {
    --backdrop: #2e2d30;
    --card-white: #f4f4f2;
    --brand-green: #86bc25;
    --brand-green-soft: #b7d978;
    --ink-grey: #5d5d5f;
    --ink-dark: #2a2a2c;
    --white: #ffffff;
    --watermark: rgba(255,255,255,0.16);
  }
  * { margin: 0; padding: 0; box-sizing: border-box; }
  html, body {
    width: 1200px; height: 774px; overflow: hidden;
    background: var(--backdrop);
    font-family: "Ubuntu", sans-serif;
  }
  .canvas { position: relative; width: 1200px; height: 774px; }

  .card {
    position: absolute;
    width: 520px; height: 300px;
    overflow: hidden;
    box-shadow: 0 10px 24px rgba(0,0,0,0.35);
  }

  /* Front card */
  .card-front { left: 60px; top: 80px; background: var(--card-white); }
  .front-logo {
    position: absolute; right: 26px; top: 22px;
    font-size: 22px; font-weight: 500; color: var(--ink-dark);
    display: flex; align-items: center; gap: 8px;
  }
  .front-logo .mark { width: 12px; height: 12px; background: var(--brand-green); }
  .contact-block {
    position: absolute; right: 26px; top: 60px;
    text-align: right; color: var(--ink-grey);
    font-size: 9px; line-height: 14px; font-weight: 400;
  }
  .contact-block .zh {
    font-family: "Noto Sans SC", sans-serif; font-size: 8.5px; color: var(--ink-dark);
  }
  .accent-square {
    position: absolute; left: 44px; top: 120px;
    width: 26px; height: 26px; background: var(--brand-green-soft);
  }
  .person { position: absolute; left: 44px; top: 156px; color: var(--ink-grey); }
  .person-name { font-size: 30px; font-weight: 400; line-height: 34px; }
  .person-title { font-size: 13px; font-weight: 300; margin-top: 2px; }
  .web-band {
    position: absolute; left: 0; right: 0; bottom: 32px; height: 32px;
    background: var(--brand-green);
    color: var(--white); font-size: 11px; letter-spacing: 7px;
    display: flex; align-items: center; justify-content: center;
  }
  .base-rule {
    position: absolute; left: 0; right: 0; bottom: 12px; height: 6px;
    background: var(--brand-green);
  }

  /* Back card */
  .card-back { left: 620px; top: 380px; background: var(--brand-green); }
  .back-square {
    position: absolute; left: 34px; top: 40px;
    width: 30px; height: 30px; background: var(--white);
  }
  .back-logo {
    position: absolute; left: 0; right: 0; top: 126px;
    text-align: center; color: var(--white);
    font-size: 38px; font-weight: 500;
  }
  .back-watermark {
    position: absolute; right: 12px; top: 30px;
    writing-mode: vertical-rl;
    color: var(--watermark);
    font-size: 40px; font-weight: 500; white-space: nowrap;
    line-height: 1;
  }
</style>
</head>
<body>
<main class="canvas">
  <section class="card card-front" aria-label="Business card front">
    <div class="front-logo"><span class="mark"></span>Brantwell Media</div>
    <div class="contact-block">
      <p class="zh">北京市 东城区 东四西路 林登商务中心</p>
      <p class="zh">410室 邮编 100010 布兰特威尔传媒</p>
      <p>Suite 410, Linden Court Business Centre</p>
      <p>Dongsi West Rd, Dongcheng District, Beijing 100010</p>
      <p>Mobile: +86 138 0012 4477 &nbsp;Email: lydia.zhou@brantwellmedia.com</p>
      <p>MSN: lydia_zh@mailbox.com &nbsp;QQ: 2048815530</p>
    </div>
    <div class="accent-square"></div>
    <div class="person">
      <p class="person-name">Lydia Zhou</p>
      <p class="person-title">Account Director</p>
    </div>
    <div class="web-band">www.brantwellmedia.com</div>
    <div class="base-rule"></div>
  </section>

  <section class="card card-back" aria-label="Business card back">
    <div class="back-square"></div>
    <div class="back-logo">Brantwell Media</div>
    <div class="back-watermark">Brantwell</div>
  </section>
</main>
</body>
</html>
```